Brusque Premium Men's Shaving Cream Product Label . Cream packaged in a Amber Jar/Black Top Cap.

Please include information ( see Brusque design Template attachment) designed on a Round Top cap. Label Diameter: 3.125" NOTE: Design this First,
Wrap Around Label: 11.3125 x 0.875" (w x h): NOTE: Required latter after selection of Final Design Selection.
Shave Cream packaged in an 8oz Low Profile Amber Jar/Black Top Cap.
Thanks

Target Market(s)

Prime Target-Men Ages 20yrs-65yrs+ and Women 20yrs-65yrs+( they purchase ovr 55% of these Mens care products for partner/spouse/friend.

Industry/Entity Type

Personel Care/Cosmetics/NaturalHealthcare

Other font styles liked:
• At this stage if you would like to submi a desigh that would include both a Top Label and your Wrap-around label on a Amber jar/black top lid. It would be helpful to see how it would look complete. Thanks . Please refer to the updated design Graphic Template for copy and layout . Questions? Let me know. Thanks.Please now use TIMBERLAND on label designs. Thanks! Please see image attachment for added Tree Image Vector that can be added to your design instead of the Original Tree Image .

Requirements
Must have
• Look and Feel of a Quality/Premium Mens Skincare Brand with a Masculine feel but attractive to women as well ( not Macho!).Think Unisex with a Male slant.
Nice to have
• Premium/Quality/Natural Skincare & Bodycare Brand
Should not have
• Not Macho. No Cartoony or Barber Tools/Bearded Men Images. Too gimicky and over-hyped!

```html
<!DOCTYPE html>
<html lang="en">
<head>
<meta charset="utf-8">
<title>Brusque Shaving Cream – Top Cap Label</title>
<link rel="stylesheet" href="https://fonts.googleapis.com/css2?family=Cinzel:wght@400;500&family=Montserrat:wght@700&display=swap">
<style>
  :root {
    --page: #ffffff;
    --navy-rim: #1c1a5c;
    --dusk-top: #7a7488;
    --dusk-mid: #3a3549;
    --night: #0e0d14;
    --silver-dark: #86878b;
    --silver-light: #c9cacc;
    --silver-mid: #9fa0a4;
    --ink: #15134a;
    --gold: #eec53a;
    --white: #ffffff;
  }
  html, body {
    margin: 0;
    width: 1200px;
    height: 1200px;
    overflow: hidden;
    background: var(--page);
  }
  .cap-label { display: block; width: 1200px; height: 1200px; }
  .line-name { font-family: "Cinzel", serif; font-size: 34px; letter-spacing: 12px; fill: var(--gold); }
  .brand-name { font-family: "Montserrat", sans-serif; font-weight: 700; font-size: 84px; letter-spacing: 18px; fill: var(--white); }
  .product-title { font-family: "Cinzel", serif; font-weight: 500; font-size: 56px; fill: var(--ink); }
  .product-subtitle { font-family: "Cinzel", serif; font-size: 38px; fill: var(--ink); }
  .scent-name { font-family: "Cinzel", serif; font-size: 28px; fill: var(--gold); }
  .year { font-family: "Cinzel", serif; font-size: 34px; fill: var(--gold); letter-spacing: 2px; }
  .net-weight { font-family: "Cinzel", serif; font-size: 23px; fill: var(--ink); }
</style>
</head>
<body>
<svg class="cap-label" viewBox="0 0 1200 1200" xmlns="http://www.w3.org/2000/svg">
  <defs>
    <linearGradient id="sky-fill" x1="0" y1="0" x2="0" y2="1">
      <stop offset="0" stop-color="var(--dusk-top)"/>
      <stop offset="0.45" stop-color="var(--dusk-mid)"/>
      <stop offset="0.9" stop-color="var(--night)"/>
    </linearGradient>
    <linearGradient id="silver-fill" x1="0" y1="0" x2="1" y2="1">
      <stop offset="0" stop-color="var(--silver-dark)"/>
      <stop offset="0.55" stop-color="var(--silver-light)"/>
      <stop offset="1" stop-color="var(--silver-mid)"/>
    </linearGradient>
    <linearGradient id="ring-stroke" x1="0" y1="0" x2="1" y2="1">
      <stop offset="0" stop-color="#d9d9dc"/>
      <stop offset="1" stop-color="#6f6f73"/>
    </linearGradient>
    <clipPath id="disc-clip"><circle cx="604" cy="591" r="378"/></clipPath>
    <path id="line-name-arc" d="M 360 591 A 244 244 0 0 1 848 591"/>
  </defs>

  <g class="disc">
    <g clip-path="url(#disc-clip)">
      <rect class="sky-band" x="220" y="210" width="770" height="470" fill="url(#sky-fill)"/>
      <rect class="silver-band" x="220" y="680" width="770" height="300" fill="url(#silver-fill)"/>
    </g>
    <circle class="outer-rim" cx="604" cy="591" r="378" fill="none" stroke="var(--navy-rim)" stroke-width="3"/>
    <circle class="inner-ring" cx="604" cy="592" r="350" fill="none" stroke="url(#ring-stroke)" stroke-width="4"/>
  </g>

  <text class="line-name" text-anchor="middle">
    <textPath href="#line-name-arc" startOffset="50%">FORESTVALE</textPath>
  </text>

  <text class="brand-name" x="604" y="600" text-anchor="middle">BRUSQUE</text>

  <text class="product-title" x="600" y="742" text-anchor="middle">Shaving Cream</text>
  <text class="product-subtitle" x="600" y="786" text-anchor="middle">Crème De Rasage</text>
  <text class="scent-name" x="600" y="836" text-anchor="middle">Oakgrove Noblesse</text>
  <g class="year-line">
    <line x1="526" y1="862" x2="548" y2="862" stroke="var(--gold)" stroke-width="3"/>
    <text class="year" x="600" y="874" text-anchor="middle">1935</text>
    <line x1="652" y1="862" x2="674" y2="862" stroke="var(--gold)" stroke-width="3"/>
  </g>
  <text class="net-weight" x="600" y="916" text-anchor="middle">150g e 5.3 oz</text>
</svg>
</body>
</html>
```